Promotional Flyer/Email Design - Cabling services for Broadcast and Audio Visual

We need a promotional flyer/email design to help launch our company, Velto Wire. We provide cabling services for Broadcast Television and Audio Visual systems. Recent projects include major television events such as the Harrowfield Racquet Open and Audio Visual/Entertainment systems for wealthy clients in their homes and on-board super yachts.

The flyer will be printed as single sided A5 and also be sent out in the body of a promotional email. It should feature the company logo along with a complementary colour scheme. It should have a clean finish with images that show the type of work we do (cabling and equipment installation) or the setting for these systems (tv studio, super yacht, cinema room, meeting room with projector etc.)

Services we offer are:

Broadcast/AV system design
On-site installation
Rack building
Pre-fabricated cable looms
Fibre optic installation

About the company:

Velto Wire provide cabling services for Broadcast Television and Audio Visual systems. With over 15 years experience working in these industries we can help with every aspect of design, project managment, installation and maintenance. Our projects range from fibre optic cabling at major sports events to installing and commisioning bespoke control systems on some of the worlds largest super yachts.

Contact details:

To get a quote or discuss your project contact us now
Telephone: TBC
Email: info@velto-wire.example
Website: www.velto-wire.example
Address: TBC

Other information:

The company is based in London, UK. Our projects often take place in other countries with work taking place accross Europe and beyond.

We have a London based workshop for rack building and cable pre-fabrication.

Our website is www.velto-wire.example

Images:

Images attached can be editted for use on the flyer or have ideas taken from them. Only the company logo is required to feature on the final design.

Target Market(s)

Business to business

Industry/Entity Type

It Company

Font styles to use
Sans Serif

Requirements
Must have
• Company logo
• List of services
• Contact details
Nice to have
• Image of cabling, home cinema room, super yacht, luxury home, outside broadcast truck, fibre optic equipment or cabling.

```html
<!DOCTYPE html>
<html lang="en">
<head>
<meta charset="utf-8">
<title>Velto Wire – Broadcast &amp; AV System Installation</title>
<link href="https://fonts.googleapis.com/css2?family=Mulish:wght@300;400&family=Roboto:wght@400;700&family=Roboto+Condensed:wght@400;700&display=swap" rel="stylesheet">
<style>
  :root{
    --red:#e2123f;
    --blue:#1f7ce3;
    --ink:#2c2c2e;
    --text:#1d1d1f;
    --panel:#eeeeef;
    --white:#ffffff;
    --backdrop:#e4e4e6;
  }
  *{margin:0;padding:0;box-sizing:border-box}
  html,body{width:1200px;height:1200px;overflow:hidden;background:var(--backdrop)}
  .canvas{position:relative;width:1200px;height:1200px}
  .flyer{position:absolute;left:196px;top:21px;width:850px;height:1218px;background:var(--white);
    transform:scale(.95);transform-origin:0 0;overflow:hidden;box-shadow:0 10px 30px rgba(0,0,0,.18);
    font-family:"Roboto",sans-serif;color:var(--text)}
  .abs{position:absolute}
  .hero-art{left:0;top:0}
  .brand{left:40px;top:62px;width:270px;display:flex;flex-direction:column;align-items:center;gap:14px}
  .brand-mark{width:90px;height:84px;background:var(--red);border-radius:8px}
  .brand-name{font-family:"Roboto",sans-serif;font-weight:700;font-size:44px;line-height:1;color:var(--ink);letter-spacing:-.5px;white-space:nowrap}
  .headline-top{left:44px;top:352px;font-family:"Mulish",sans-serif;font-weight:300;font-size:38px;letter-spacing:1px;color:var(--ink)}
  .headline-main{left:42px;top:398px;font-family:"Roboto Condensed",sans-serif;font-weight:400;font-size:80px;color:var(--red);letter-spacing:-1px;line-height:1}
  .headline-sub{left:44px;top:484px;font-family:"Roboto Condensed",sans-serif;font-weight:700;font-size:63px;color:var(--blue);letter-spacing:1.5px;line-height:1}
  .about-rule{left:0;top:570px;width:850px;height:8px;background:var(--red)}
  .about-band{left:0;top:578px;width:850px;height:149px;background:var(--ink)}
  .about-pill{left:262px;top:575px;width:328px;height:42px;border-radius:21px;background:var(--red);color:var(--white);
    font-family:"Roboto Condensed",sans-serif;font-weight:700;font-size:21px;letter-spacing:.5px;display:flex;align-items:center;justify-content:center}
  .about-text{left:55px;top:632px;width:742px;color:var(--white);font-size:15.4px;line-height:19px;text-align:justify;text-align-last:center;letter-spacing:-.1px}
  .panel-left{left:0;top:727px;width:413px;height:471px;background:var(--panel)}
  .panel-divider{left:413px;top:727px;width:7px;height:471px;background:var(--ink)}
  .panel-right{left:420px;top:727px;width:430px;height:471px;background:linear-gradient(90deg,#f3f3f4,#fbfbfb)}
  .section-title{font-family:"Roboto Condensed",sans-serif;font-weight:700;font-size:22px;color:var(--red);letter-spacing:.5px}
  .services-title{left:54px;top:738px}
  .service{left:54px;height:33px;border:1.5px solid var(--red);border-radius:17px;display:flex;align-items:center;
    padding-right:12px;font-family:"Mulish",sans-serif;font-size:20px;color:var(--ink);letter-spacing:.3px}
  .service-icon{width:33px;height:33px;border-radius:50%;background:var(--red);margin:-1.5px 12px 0 -1.5px;display:flex;align-items:center;justify-content:center;flex:none}
  .service-icon span{width:17px;height:17px;border-radius:50%;border:2px solid var(--white)}
  .service-photo{left:62px;top:1026px;width:328px;height:152px;border-radius:22px;
    background:linear-gradient(135deg,#d8cbb8 0%,#b9a68e 45%,#8d7a66 100%)}
  .photo-accent{left:56px;top:1018px}
  .quote-lead{left:446px;top:748px;width:340px;font-family:"Mulish",sans-serif;font-size:17px;line-height:22px;color:var(--ink);letter-spacing:.3px}
  .quote-rule{left:446px;top:796px;width:130px;height:1.5px;background:var(--ink)}
  .contact{left:446px;display:flex;align-items:center;gap:12px;font-family:"Mulish",sans-serif;font-size:17px;color:var(--ink)}
  .contact svg{flex:none}
  .other-title{left:444px;top:967px}
  .other-text{left:444px;top:999px;width:350px;font-size:17.4px;line-height:21.5px;text-align:justify;color:var(--text)}
  .other-text p{margin-bottom:8px}
  .other-text p.last{text-align:left}
  .web-link{color:var(--blue);font-weight:700;font-style:italic;border-bottom:2px solid var(--red)}
  .base-band{left:0;top:1198px;width:850px;height:20px;background:var(--blue)}
</style>
</head>
<body>
<div class="canvas">
  <div class="flyer">

    <svg class="abs hero-art" width="850" height="570" viewBox="0 0 850 570" aria-hidden="true">
      <path d="M0 300 L18 322 C90 268 200 238 330 232 L330 244 C210 250 110 282 32 332 L18 330 Z" fill="#e2123f"/>
      <path d="M36 332 C110 286 200 260 312 252 C220 266 130 296 58 340 Z" fill="#2c2c2e"/>
      <circle cx="668" cy="188" r="342" fill="none" stroke="#1f7ce3" stroke-width="10"/>
      <circle cx="668" cy="188" r="336" fill="#ffffff"/>
    </svg>
    <svg class="abs" style="left:0;top:0" width="850" height="570" viewBox="0 0 850 570" role="img" aria-label="Photo of a home cinema room with a projection screen, curtains and a lounge chair">
      <defs>
        <linearGradient id="cinema" x1="0" y1="0" x2="0" y2="1">
          <stop offset="0" stop-color="#8a7a66"/>
          <stop offset=".45" stop-color="#6e5c4a"/>
          <stop offset="1" stop-color="#4a3a2e"/>
        </linearGradient>
      </defs>
      <circle cx="668" cy="178" r="332" fill="url(#cinema)"/>
    </svg>

    <div class="abs brand"><span class="brand-mark"></span><span class="brand-name">Velto Wire</span></div>

    <div class="abs headline-top">Broadcast &amp;</div>
    <div class="abs headline-main">AV System</div>
    <div class="abs headline-sub">INSTALLATION</div>

    <div class="abs about-rule"></div>
    <div class="abs about-band"></div>
    <div class="abs about-pill">ABOUT THE COMPANY:</div>
    <p class="abs about-text">Velto Wire provide cabling services for Broadcast Television and Audio Visual systems. With over 15 years experience working in these industries we can help with every aspect of design, project managment, installation and maintenance. Our projects range from fibre optic cabling at major sports events to installing and commisioning bespoke control systems on some of the worlds largest super yachts.</p>

    <div class="abs panel-left"></div>
    <div class="abs panel-divider"></div>
    <div class="abs panel-right"></div>

    <div class="abs section-title services-title">SERVICES:</div>
    <div class="abs service" style="top:778px"><span class="service-icon"><span></span></span>Broadcast/AV system design</div>
    <div class="abs service" style="top:828px"><span class="service-icon"><span></span></span>On-site installation</div>
    <div class="abs service" style="top:878px"><span class="service-icon"><span></span></span>Rack building</div>
    <div class="abs service" style="top:927px"><span class="service-icon"><span></span></span>Pre-fabricated cable looms</div>
    <div class="abs service" style="top:977px;width:330px"><span class="service-icon"><span></span></span>Fibre optic installation</div>

    <svg class="abs photo-accent" width="340" height="166" viewBox="0 0 340 166" aria-hidden="true">
      <path d="M8 152 C30 164 80 164 310 164 C326 164 334 150 334 130 L334 30 C334 14 326 6 304 8 C250 10 200 6 150 10" fill="none" stroke="#e2123f" stroke-width="3"/>
    </svg>
    <div class="abs service-photo" role="img" aria-label="Photo of a luxury living room with a wall-mounted television and sofas"></div>

    <p class="abs quote-lead">To get a quote or discuss your project contact us now</p>
    <div class="abs quote-rule"></div>

    <div class="abs contact" style="top:812px">
      <svg width="16" height="16" viewBox="0 0 24 24"><path fill="#e2123f" d="M6.6 10.8a15 15 0 0 0 6.6 6.6l2.2-2.2c.3-.3.7-.4 1-.2 1.1.4 2.300.6 3.6.6.6 0 1 .4 1 1V20c0 .6-.4 1-1 1A17 17 0 0 1 3 4c0-.6.4-1 1-1h3.5c.6 0 1 .4 1 1 0 1.3.2 2.5.6 3.6.1.3 0 .7-.2 1z"/></svg>
      <span>TBC</span></div>
    <div class="abs contact" style="top:845px">
      <svg width="16" height="16" viewBox="0 0 24 24"><circle cx="12" cy="12" r="11" fill="#e2123f"/><rect x="6" y="8" width="12" height="8" fill="none" stroke="#fff" stroke-width="1.6"/><path d="M6 8l6 5 6-5" fill="none" stroke="#fff" stroke-width="1.6"/></svg>
      <span>info@velto-wire.example</span></div>
    <div class="abs contact" style="top:883px">
      <svg width="16" height="16" viewBox="0 0 24 24"><circle cx="12" cy="12" r="11" fill="#e2123f"/><path d="M1 12h22M12 1c4 4 4 18 0 22M12 1c-4 4-4 18 0 22" fill="none" stroke="#fff" stroke-width="1.4"/></svg>
      <span>www.velto-wire.example</span></div>
    <div class="abs contact" style="top:915px">
      <svg width="16" height="16" viewBox="0 0 24 24"><path fill="#e2123f" d="M12 1a7 7 0 0 0-7 7c0 5 7 13 7 13s7-8 7-13a7 7 0 0 0-7-7zm0 9.5A2.5 2.5 0 1 1 12 5.5a2.5 2.5 0 0 1 0 5z"/><rect x="4" y="21" width="16" height="2" fill="#e2123f"/></svg>
      <span>TBC</span></div>

    <div class="abs section-title other-title">OTHER INFORMATION:</div>
    <div class="abs other-text">
      <p>The company is based in London, UK. Our projects often take place in other countries with work taking place accross Europe and beyond.</p>
      <p class="last">We have a London based workshop for rack building and cable pre-fabrication.</p>
      <p class="last">Our website is <span class="web-link">www.velto-wire.example</span></p>
    </div>

    <div class="abs base-band"></div>
  </div>
</div>
</body>
</html>
```